The Quiet Compass
Zielgruppe
Das Bundesforum Seelenheilkundiger Praxen e. V. (BFSP) ist ein Interessenverband mit 1.400 Mitgliedern, der sich für die Belange von psychotherapeutisch tätigen Psychologen, Ärzten und Kinder- und Jugendlichen-Psychotherapeuten einsetzt. Das Bundesforum Seelenheilkundiger Praxen wurde als Berufsverband am 2. Mai 2019 in Bonn gegründet.
Aufgabenstellung
Titel: The Quiet Compass - Das Arbeitsbuch der selten genutzten und vergessenen therapeutischen Werkzeuge im Behandlungsalltag
Kategorie: Sachbuch
Zielgruppe: nur Psychotherapeuten
Covergestaltung: Cover soll neugierig machen, aber nicht marktschreierisch sein, AIDA-Regel berücksichtigen,
„Augenfänger“, dezente Farben, nicht zu grell
Buchformat: 22x15.5 cm, ca. 530 Normseiten
Buchrücken: Titel und Autor
Ausführung: Hardcover, Softcover, Ebook
Autor: Rainer Holtkamp, Dipl.-Psychologe, ist Psychoanalytiker der Westfälischen Tiefenseelischen Gesellschaft, Kinder- und Jugendlichenpsychotherapeut, Psychologischer Psychotherapeut, Gruppenanalytiker, Lehrtherapeut und Supervisor. Neben seiner psychoanalytischen Ausbildung hat er noch Aus- und Weiterbildungen in Gruppentherapie, Gruppendynamik, Familientherapie, katathym imaginativer Psychotherapie und intensiver psychodynamischer Kurztherapie nach Davanloo. Seit 29 Jahren arbeitet er in seiner eigenen Praxis in Bonn. Neben seiner Praxistätigkeit arbeitet er als Gutachter im Antragsverfahren der gesetzlichen Krankenkassen und der Beihilfestellen. Er ist Gründer und 1. Vorsitzender des Bundesforums Seelenheilkundiger Praxen (BFSP) in Bonn.
Klappentext: „Wer liebt, was er tut, wird nie wieder arbeiten müssen.“ Ein kluger Aphorismus, der Konfuzius zugeschrieben wird. Psychotherapeuten lieben ihren Beruf. Dennoch ist die Arbeit mit kranken Menschen immer schwer und unberechenbar. Viele Erfahrungen und Erkenntnisse musste sich Rainer Holtkamp im Laufe seiner Berufstätigkeit von fast 30 Jahren selbst erarbeiten. In seiner Tätigkeit als Dozent und Supervisor konnte er viele Fragen der Kandidaten sammeln und daraus Interventionen erarbeiten. Interventionen, die meist in keinem Lehrbuch stehen. Mit vielen dieser Interventionen wird die psychotherapeutische Arbeit leichter und macht auch mehr Freude. Und wer mit Freude als Psychotherapeut in die Praxis geht, 'arbeitet' im Sinne ..

```html
<!DOCTYPE html>
<html lang="de">
<head>
<meta charset="utf-8">
<title>The Quiet Compass – Buchcover</title>
<link rel="stylesheet" href="https://fonts.googleapis.com/css2?family=Permanent+Marker&family=Patrick+Hand&family=Didact+Gothic&display=swap">
<style>
  :root {
    --page-bg: #efefef;
    --cover-teal: #3ca3a6;
    --title-white: #ffffff;
    --subtitle-ink: #1d2a2d;
    --art-sky: #8fc4c2;
    --art-sun: #e6d86a;
    --art-couch: #b58f5e;
    --art-figure: #7fa8d6;
  }
  * { margin: 0; padding: 0; box-sizing: border-box; }
  html, body {
    width: 1200px;
    height: 1062px;
    overflow: hidden;
    background: var(--page-bg);
  }
  .book-cover {
    position: absolute;
    left: 246px;
    top: 31px;
    width: 707px;
    height: 1000px;
    background: var(--cover-teal);
  }
  .title-art {
    position: absolute;
    left: 0;
    top: 0;
    width: 707px;
    height: 340px;
  }
  .title-art text {
    font-family: "Permanent Marker", cursive;
    fill: var(--title-white);
  }
  .subtitle {
    position: absolute;
    left: 0;
    top: 284px;
    width: 707px;
    text-align: center;
    font-family: "Patrick Hand", cursive;
    font-size: 25px;
    line-height: 37px;
    text-transform: uppercase;
    color: var(--subtitle-ink);
  }
  .cover-illustration {
    position: absolute;
    left: 130px;
    top: 461px;
    width: 463px;
    height: 320px;
  }
  .author-name {
    position: absolute;
    left: 0;
    top: 908px;
    width: 707px;
    text-align: center;
    font-family: "Didact Gothic", sans-serif;
    font-size: 29px;
    letter-spacing: 0.16em;
    color: var(--title-white);
    text-transform: uppercase;
  }
</style>
</head>
<body>
  <main class="book-cover">
    <svg class="title-art" viewBox="0 0 707 340" aria-label="The Quiet Compass">
      <defs>
        <path id="title-arc" d="M 60 325 Q 353 55 650 325"/>
      </defs>
      <text x="353" y="138" font-size="62" text-anchor="middle">THE</text>
      <text font-size="80">
        <textPath href="#title-arc" startOffset="50%" text-anchor="middle">QUIET COMPASS</textPath>
      </text>
    </svg>

    <p class="subtitle">
      Das Arbeitsbuch<br>
      der selten genutzten<br>
      und vergessenen therapeutischen Werkzeuge<br>
      im Behandlungsalltag
    </p>

    <svg class="cover-illustration" viewBox="0 0 463 320" role="img"
         aria-label="Illustration: Person ruht auf einer Chaiselongue vor einer aufgehenden Sonne">
      <defs>
        <linearGradient id="illustration-tones" x1="0" y1="0" x2="0" y2="1">
          <stop offset="0" stop-color="var(--art-sky)"/>
          <stop offset="0.45" stop-color="var(--art-sun)"/>
          <stop offset="0.7" stop-color="var(--art-figure)"/>
          <stop offset="1" stop-color="var(--art-couch)"/>
        </linearGradient>
      </defs>
      <rect width="463" height="320" rx="40" fill="url(#illustration-tones)" opacity="0.85"/>
    </svg>

    <p class="author-name">Autor Name</p>
  </main>
</body>
</html>
```